Juice Label for Hispanic Customer Demographic

We need a label design for two related Juice items. Brand name will be "Cidrovel" The first item is a Lemon Juice Blend and the second is a lime juice. We would like to see designs that focus on a target market that is mainly first and second generation Hispanic immigrants. Heavily Spanish speaking and price conscious.

Product will be packaged in 32 oz flip to bottle with wrap around label. Both SKU’s will have the same size and design with one showing Lemons and the other showing Limes similar to the examples attached. The bottle will be green with a green cap for the lime juice and a yellow cap for the lemon juice.

I have attached Dielines and some images of a similar product for reference.

Target Market(s)

Hispanic shopper, mainly first and second generation immigrants. Heavily Spanish speaking demographic. Price conscious.

Industry/Entity Type

Grocery Store

Font styles to use
Sans Serif

Colors
ffcf3e
abd036
fbf289
fbee3e

Requirements
Must have
• Product Name—
• • “Cidrovel Lemon Juice Blend” -- 54% Juice
• • “Cidrovel Lime Juice “-- 25% Juice
• Please include copy-
• Note: Product name and required copy below should be in English. Additional copy can be either English or Spanish.
• • “Made in the USA”
• • “From Concentrate”
• • “Naturally Reconstituted”
• • “Refrigerate after opening”
• • “Shake Well!”
• • “Net 32 Fl OZ (1QT) 946 ml”
• Please include a space for the nutrition facts should be :
• 4 8/10 cm H x 3 8/10 cm W.
• Include a white space for the scan bar 1/7/10 cm H x 3/2/10 cm W. (?? Dimensions)
• Please use ingredient lists as below-
• Lemon Juice--
• INGREDIENTS: FILTERED WATER, LEMON
• JUICE CONCENTRATE, CITRIC ACID, ESTER
• GUM, LEMON OIL, SODIUM BENZOATE (AS
• PRESERVATIVE), SODIUM BISULFITE (AS
• PRESERVATIVE).
• Lime Juice--
• INGREDIENTS: FILTERED WATER, LIME JUICE CONCENTRATE, CITRIC ACID,
• ESTER GUM, LIME OIL, SODIUM BENZOATE (AS PRESERVATIVE), SODIUM BISULFITE (AS A PRESERVATIVE)
Nice to have
• Would like to have an image of fruit very prominent in the design. This image can be either a drawing or a photograph.

```html
<!DOCTYPE html>
<html lang="en">
<head>
<meta charset="utf-8">
<title>Cidrovel Juice Labels</title>
<link rel="stylesheet" href="https://fonts.googleapis.com/css2?family=Alfa+Slab+One&family=Open+Sans:wght@400;700&display=swap">
<style>
  :root {
    --canvas-bg: #eeeeec;
    --lemon-light: #fbf289;
    --lemon-mid: #fbee3e;
    --lemon-deep: #ffcf3e;
    --lime-light: #c9e05a;
    --lime-mid: #abd036;
    --lime-deep: #7fae22;
    --ink-green: #2f5a1a;
    --band-green: #4d7a25;
    --band-yellow: #fbee3e;
    --white: #ffffff;
  }
  * { box-sizing: border-box; margin: 0; padding: 0; }
  html, body { width: 1200px; height: 1000px; overflow: hidden; }
  body {
    background: var(--canvas-bg);
    font-family: "Open Sans", Arial, sans-serif;
    display: flex;
    align-items: center;
    justify-content: center;
    gap: 80px;
  }
  .label {
    width: 440px;
    height: 560px;
    position: relative;
    overflow: hidden;
    display: flex;
    flex-direction: column;
    align-items: center;
    color: var(--ink-green);
  }
  .label--lemon {
    background: radial-gradient(circle at 50% 30%, var(--lemon-light) 0%, var(--lemon-mid) 45%, var(--lemon-deep) 100%);
  }
  .label--lime {
    background: radial-gradient(circle at 50% 30%, var(--lime-light) 0%, var(--lime-mid) 50%, var(--lime-deep) 100%);
  }
  .fruit-art {
    width: 330px;
    height: 250px;
    margin-top: 40px;
    border-radius: 50% 50% 46% 46%;
  }
  .label--lemon .fruit-art {
    background: radial-gradient(ellipse at 40% 40%, #fff27a 0%, #f7d21c 55%, #e8a614 100%);
  }
  .label--lime .fruit-art {
    background: radial-gradient(ellipse at 40% 40%, #9ad648 0%, #4f9a2a 60%, #2e6b1c 100%);
  }
  .brand-name {
    position: absolute;
    top: 108px;
    left: 0;
    right: 0;
    text-align: center;
    font-family: "Alfa Slab One", Georgia, serif;
    font-size: 62px;
    color: var(--ink-green);
    letter-spacing: 1px;
  }
  .label--lime .brand-name { color: #1f4512; }
  .product-name {
    margin-top: 26px;
    font-family: "Alfa Slab One", Georgia, serif;
    font-size: 30px;
    line-height: 1.1;
  }
  .juice-percent {
    font-family: "Alfa Slab One", Georgia, serif;
    font-size: 28px;
    line-height: 1.2;
  }
  .net-content {
    margin-top: 6px;
    font-size: 13px;
    font-weight: 700;
    letter-spacing: 0.3px;
  }
  .info-band {
    margin-top: 16px;
    width: 100%;
    padding: 7px 0;
    display: flex;
    justify-content: center;
    gap: 14px;
    font-size: 12px;
    font-weight: 700;
    letter-spacing: 0.4px;
  }
  .label--lemon .info-band { background: var(--band-green); color: var(--band-yellow); }
  .label--lime .info-band { background: var(--band-yellow); color: var(--ink-green); }
  .info-band .divider { opacity: 0.8; }
  .origin {
    margin-top: 20px;
    font-size: 11px;
  }
</style>
</head>
<body>
  <section class="label label--lemon">
    <div class="fruit-art" role="img" aria-label="Illustration of a whole lemon and a lemon half with leaves"></div>
    <div class="brand-name">Cidrovel</div>
    <h1 class="product-name">Lemon Juice Blend</h1>
    <p class="juice-percent">54% Juice</p>
    <p class="net-content">NET 32 FL OZ (1QT) 946 ML</p>
    <div class="info-band">
      <span>NATURALLY RECONSTITUTED</span><span class="divider">|</span><span>REFRIGERATE AFTER OPENING</span>
    </div>
    <p class="origin">Made in the USA</p>
  </section>

  <section class="label label--lime">
    <div class="fruit-art" role="img" aria-label="Illustration of a whole lime and a lime half with leaves"></div>
    <div class="brand-name">Cidrovel</div>
    <h1 class="product-name">Lime Juice</h1>
    <p class="juice-percent">25% Juice</p>
    <p class="net-content">NET 32 FL OZ (1QT) 946 ML</p>
    <div class="info-band">
      <span>NATURALLY RECONSTITUTED</span><span class="divider">|</span><span>REFRIGERATE AFTER OPENING</span>
    </div>
    <p class="origin">Made in the USA</p>
  </section>
</body>
</html>
```